Harbor Lanterns: Walking Beside Young Ones Through Every Season

This book is about being a good father and how to parent them well so they are fully equipped to launch into the world when they become adults. It is an encouraging and practical guide that acknowledges the difficulties of being a good father and provides strategies for addressing them.

Target Market(s)

My target market is dads, or people that will gift this book to a dad that they know

```html
<!DOCTYPE html>
<html lang="en">
<head>
<meta charset="UTF-8">
<title>Harbor Lanterns – Book Cover</title>
<link href="https://fonts.googleapis.com/css2?family=Montserrat:wght@400;500;600;800&display=swap" rel="stylesheet">
<style>
  :root {
    --canvas-bg: #e7e5e1;
    --cover-top: #f0efed;
    --cover-mid: #e9e6e3;
    --spine-light: #f7f7f6;
    --spine-shade: #d6d4d2;
    --title-brown: #4b2a22;
    --subtitle-brown: #3d2a25;
    --sky-warm: #e4dcd5;
    --horizon: #c9a98f;
    --field-gold: #a0704c;
    --field-rust: #7a4328;
    --field-deep: #5a2f1c;
    --field-dark: #36180f;
    --author-white: #ffffff;
  }
  * { margin: 0; padding: 0; box-sizing: border-box; }
  html, body {
    width: 1200px;
    height: 1200px;
    overflow: hidden;
    background: var(--canvas-bg);
  }
  .canvas {
    position: relative;
    width: 1200px;
    height: 1200px;
    display: flex;
    align-items: center;
    justify-content: center;
  }
  .book-cover {
    position: relative;
    width: 810px;
    height: 1140px;
    overflow: hidden;
    background: linear-gradient(180deg, var(--cover-top) 0%, var(--cover-mid) 100%);
    font-family: "Montserrat", sans-serif;
  }
  .spine-hinge {
    position: absolute;
    top: 0;
    left: 0;
    width: 70px;
    height: 100%;
    background: linear-gradient(90deg, var(--spine-shade) 0%, var(--spine-light) 35%, var(--spine-light) 70%, var(--spine-shade) 100%);
    opacity: 0.8;
    z-index: 3;
  }
  .field-photo {
    position: absolute;
    left: 0;
    right: 0;
    top: 330px;
    bottom: 0;
    background:
      radial-gradient(ellipse 22% 55% at 62% 100%, rgba(140, 80, 50, 0.45) 0%, rgba(140, 80, 50, 0) 100%),
      linear-gradient(172deg,
        rgba(233, 230, 227, 0) 0%,
        var(--sky-warm) 34%,
        var(--horizon) 41%,
        var(--field-gold) 45%,
        var(--field-rust) 58%,
        var(--field-deep) 78%,
        var(--field-dark) 100%);
    z-index: 1;
  }
  .title-block {
    position: absolute;
    top: 78px;
    left: 110px;
    right: 50px;
    z-index: 4;
    color: var(--title-brown);
  }
  .title-top {
    display: block;
    font-size: 62px;
    font-weight: 500;
    letter-spacing: 0.28em;
    line-height: 1;
  }
  .title-main {
    display: block;
    font-size: 96px;
    font-weight: 800;
    letter-spacing: 0.01em;
    line-height: 1.05;
    margin-top: 6px;
  }
  .subtitle {
    margin-top: 14px;
    font-size: 23px;
    font-weight: 500;
    color: var(--subtitle-brown);
    line-height: 1.3;
  }
  .author-name {
    position: absolute;
    left: 70px;
    right: 0;
    bottom: 110px;
    text-align: center;
    font-size: 27px;
    font-weight: 600;
    letter-spacing: 0.03em;
    color: var(--author-white);
    z-index: 4;
  }
</style>
</head>
<body>
  <main class="canvas">
    <article class="book-cover">
      <div class="spine-hinge"></div>
      <h1 class="title-block">
        <span class="title-top">HARBOR</span>
        <span class="title-main">LANTERNS</span>
        <span class="subtitle">Walking Beside Young Ones Through Every Season</span>
      </h1>
      <div class="field-photo" role="img" aria-label="Photograph of a father flying a kite with his young son on a dirt path through a golden grassy field under a pale evening sky"></div>
      <p class="author-name">AUTHOR NAME</p>
    </article>
  </main>
</body>
</html>
```